Plakate für Podologie - Medizinische Fusspflege
Zielgruppe
Podologie - Medizinische Fusspflege. Zielgruppe sind Kinder bis und mit ältere Menschen.
Aufgabenstellung
Möchte ein modernes, aber auch klassisches Design, dass Professionalität & medizinische Fundiertheit ausstrahlt. Man soll sehen, dass es medizinisch ist und nicht verwechselbar mit kosmetischer Fusspflege.

```html
<!DOCTYPE html>
<html lang="de">
<head>
<meta charset="utf-8">
<title>PediNova – Medizinische Podologie</title>
<link href="https://fonts.googleapis.com/css2?family=Hind:wght@400;500;600&family=Roboto:wght@400;700&family=Roboto+Condensed:wght@700&display=swap" rel="stylesheet">
<style>
  :root{
    --teal-dark:#135a57;
    --teal:#1d716c;
    --teal-light:#2b8f87;
    --grey:#6b6f70;
    --white:#ffffff;
    --skin:#f2d4c2;
    --skin-light:#f8e8de;
  }
  *{margin:0;padding:0;box-sizing:border-box}
  html,body{width:848px;height:1200px;overflow:hidden;background:var(--white)}
  .poster{position:relative;width:848px;height:1200px;overflow:hidden;background:var(--white);font-family:"Hind",sans-serif;color:var(--teal-dark)}

  .brand-dot{position:absolute;left:56px;top:60px;width:80px;height:80px;border-radius:50%;background:var(--teal-dark)}
  .brand-name{position:absolute;left:160px;top:78px;font-family:"Hind",sans-serif;font-weight:500;font-size:62px;line-height:1;color:var(--teal-dark)}
  .brand-tagline{position:absolute;left:164px;top:146px;font-family:"Hind",sans-serif;font-weight:500;font-size:16.5px;letter-spacing:2.6px;color:var(--grey)}

  .badge{position:absolute;left:631px;top:0;width:180px;height:170px;background:var(--teal);border-radius:0 0 14px 14px;padding:26px 0 0 19px;color:var(--white)}
  .badge-title{font-family:"Roboto",sans-serif;font-weight:700;font-size:20.5px;line-height:25px;letter-spacing:.4px}
  .badge-list{list-style:none;font-family:"Roboto",sans-serif;font-size:17px;line-height:20.5px;margin-top:8px}

  .photo{position:absolute;left:360px;top:330px;width:488px;height:540px;
    background:
      radial-gradient(ellipse 55% 45% at 55% 58%, var(--skin) 0%, var(--skin-light) 55%, rgba(255,255,255,0) 100%),
      radial-gradient(ellipse 60% 55% at 80% 35%, #eef0f2 0%, rgba(255,255,255,0) 100%);}

  .headline{position:absolute;left:60px;top:250px;font-family:"Hind",sans-serif;font-weight:500;font-size:66px;line-height:65px;letter-spacing:.5px;color:var(--teal-dark)}
  .subline{position:absolute;left:62px;top:382px;font-family:"Hind",sans-serif;font-weight:500;font-size:27.5px;line-height:34px;color:var(--teal-dark)}

  .services{position:absolute;left:64px;top:496px;list-style:none}
  .services li{display:flex;align-items:flex-start;height:55.5px;font-family:"Hind",sans-serif;font-weight:500;font-size:21.5px;line-height:28px;color:var(--teal-dark)}
  .services li svg{flex:none;width:44px;height:44px;margin-right:12px}
  .services li span{padding-top:18px}
  .services li.two-line span{padding-top:15px}

  .wave{position:absolute;left:0;top:0;width:848px;height:1200px}

  .cta{position:absolute;left:544px;top:844px;width:192px;height:192px;border-radius:50%;background:var(--teal-dark);border:7px solid var(--white);display:flex;align-items:center;justify-content:center}
  .cta-text{font-family:"Roboto",sans-serif;font-weight:700;font-size:27px;line-height:31px;text-align:center;color:var(--white);transform:rotate(-8deg);letter-spacing:.8px}

  .contact{position:absolute;left:54px;top:991px;list-style:none}
  .contact li{display:flex;align-items:center;height:61px;font-family:"Hind",sans-serif;font-size:22.5px;line-height:25px;color:var(--white)}
  .contact .icon{flex:none;width:46px;height:46px;border-radius:50%;background:var(--white);display:flex;align-items:center;justify-content:center;margin-right:18px}
  .contact .icon svg{width:28px;height:28px}

  .divider{position:absolute;left:350px;top:1045px;width:1.5px;height:112px;background:rgba(255,255,255,.8)}
  .claim{position:absolute;left:390px;top:1078px;width:444px;text-align:center;font-family:"Roboto Condensed",sans-serif;font-weight:700;font-size:33px;line-height:39px;color:var(--white);white-space:nowrap}
</style>
</head>
<body>
<div class="poster">

  <div class="photo" role="img" aria-label="Foto: behandschuhte Hände untersuchen die Zehen eines Fusses"></div>

  <div class="brand-dot"></div>
  <div class="brand-name">PediNova</div>
  <div class="brand-tagline">MEDIZINISCHE PODOLOGIE</div>

  <div class="badge">
    <div class="badge-title">ZERTIFIZIERTE<br>PODOLOGEN</div>
    <ul class="badge-list">
      <li>Fachgerecht</li>
      <li>Hygienisch</li>
      <li>Modern</li>
    </ul>
  </div>

  <h1 class="headline">IHRE FÜSSE.<br>UNSERE KOMPETENZ.</h1>
  <p class="subline">Medizinische Fussbehandlungen<br>für Ihre Gesundheit und Lebensqualität.</p>

  <ul class="services">
    <li><svg viewBox="0 0 44 44"><path d="M36 17.5A15.5 15.5 0 1 1 28 8.3" fill="none" stroke="var(--teal-dark)" stroke-width="2.6" stroke-linecap="round"/><path d="M12 20l8 9L39 6" fill="none" stroke="var(--teal-dark)" stroke-width="4" stroke-linecap="round" stroke-linejoin="round"/></svg><span>Medizinische Fusspflege</span></li>
    <li><svg viewBox="0 0 44 44"><path d="M36 17.5A15.5 15.5 0 1 1 28 8.3" fill="none" stroke="var(--teal-dark)" stroke-width="2.6" stroke-linecap="round"/><path d="M12 20l8 9L39 6" fill="none" stroke="var(--teal-dark)" stroke-width="4" stroke-linecap="round" stroke-linejoin="round"/></svg><span>Nagelkorrektur</span></li>
    <li><svg viewBox="0 0 44 44"><path d="M36 17.5A15.5 15.5 0 1 1 28 8.3" fill="none" stroke="var(--teal-dark)" stroke-width="2.6" stroke-linecap="round"/><path d="M12 20l8 9L39 6" fill="none" stroke="var(--teal-dark)" stroke-width="4" stroke-linecap="round" stroke-linejoin="round"/></svg><span>Eingewachsene Nägel</span></li>
    <li><svg viewBox="0 0 44 44"><path d="M36 17.5A15.5 15.5 0 1 1 28 8.3" fill="none" stroke="var(--teal-dark)" stroke-width="2.6" stroke-linecap="round"/><path d="M12 20l8 9L39 6" fill="none" stroke="var(--teal-dark)" stroke-width="4" stroke-linecap="round" stroke-linejoin="round"/></svg><span>Hornhaut &amp; Hühneraugen</span></li>
    <li><svg viewBox="0 0 44 44"><path d="M36 17.5A15.5 15.5 0 1 1 28 8.3" fill="none" stroke="var(--teal-dark)" stroke-width="2.6" stroke-linecap="round"/><path d="M12 20l8 9L39 6" fill="none" stroke="var(--teal-dark)" stroke-width="4" stroke-linecap="round" stroke-linejoin="round"/></svg><span>Diabetische Fussversorgung</span></li>
    <li class="two-line"><svg viewBox="0 0 44 44"><path d="M36 17.5A15.5 15.5 0 1 1 28 8.3" fill="none" stroke="var(--teal-dark)" stroke-width="2.6" stroke-linecap="round"/><path d="M12 20l8 9L39 6" fill="none" stroke="var(--teal-dark)" stroke-width="4" stroke-linecap="round" stroke-linejoin="round"/></svg><span>Präventive Fussuntersuchung<br>und Fusspflege</span></li>
  </ul>

  <svg class="wave" viewBox="0 0 848 1200" aria-hidden="true">
    <defs>
      <linearGradient id="band" x1="0" y1="0" x2="1" y2="0">
        <stop offset="0" stop-color="#135a57"/>
        <stop offset=".55" stop-color="#1b6e69"/>
        <stop offset="1" stop-color="#2b8f87"/>
      </linearGradient>
    </defs>
    <path d="M0 826 C 180 905, 420 968, 848 990 L848 1200 L0 1200 Z" fill="var(--teal-light)"/>
    <path d="M0 852 C 200 930, 440 990, 848 1008 L848 1200 L0 1200 Z" fill="url(#band)"/>
  </svg>

  <div class="cta"><div class="cta-text">JETZT<br>TERMIN<br>SICHERN!</div></div>

  <ul class="contact">
    <li><span class="icon"><svg viewBox="0 0 24 24"><path d="M6.6 2.8c.6-.3 1.3-.1 1.6.5l1.7 3.4c.3.6.1 1.2-.4 1.6L8 9.3c.9 2.3 2.6 4.2 4.9 5.4l1.1-1.4c.4-.5 1.1-.6 1.6-.3l3.3 1.9c.6.3.8 1 .5 1.6l-1 2c-.5.9-1.5 1.4-2.5 1.2C9.5 18.6 4.9 13.9 3.8 7.6c-.2-1 .3-2 1.2-2.5z" fill="var(--teal-dark)"/></svg></span>04521 73 96 40 2</li>
    <li><span class="icon"><svg viewBox="0 0 24 24" fill="none" stroke="var(--teal-dark)" stroke-width="1.6"><circle cx="12" cy="12" r="9"/><ellipse cx="12" cy="12" rx="4" ry="9"/><path d="M3 12h18M4.5 7.5h15M4.5 16.5h15M12 3v18"/></svg></span>www.pedinova.de</li>
    <li><span class="icon"><svg viewBox="0 0 24 24"><path d="M12 2a7 7 0 0 0-7 7c0 5 7 13 7 13s7-8 7-13a7 7 0 0 0-7-7zm0 9.5A2.5 2.5 0 1 1 12 6.5a2.5 2.5 0 0 1 0 5z" fill="var(--teal-dark)"/></svg></span>Lindenweg 47<br>54321 Talheim</li>
  </ul>

  <div class="divider"></div>
  <p class="claim">AUCH FÜR RISIKOPATIENTEN,<br>KINDER UND SPORTLER</p>

</div>
</body>
</html>
```